Boutique Store Selling Antiques and Unique Finds

I need a Web Page designed for my Store Called "Larkmoor Lane". I would like a very classic, muted design that looks European when pulled up. I will be selling Antiques from all over the world and Unique finds that have reproduced. I will also be selling high-end purses and jewelry with unique, reasonable products for the every-day buyer as well.

Target Market(s)

25-70 year old men and women;)

Coding

Coded - Design and coding required

Number of Pages Required

1 page

Colors

Designer to choose only greyscale colors for use in the design.

Requirements
Must have
• I want it

```html
<!DOCTYPE html>
<html lang="en">
<head>
<meta charset="utf-8">
<title>Larkmoor Lane — Antiques &amp; Beautiful Finds</title>
<link href="https://fonts.googleapis.com/css2?family=Roboto+Slab:wght@300;400;700&family=Playfair+Display:ital@1&family=Cinzel:wght@500&family=Open+Sans:wght@400;600&display=swap" rel="stylesheet">
<style>
:root{
  --page:#f3f3f3;
  --ink:#3a3a3a;
  --muted:#8a8a8a;
  --gold:#c49a5c;
  --rule:#cfcfcf;
  --band:#eeeae7;
  --footer:#2b2b2b;
  --footer-ink:#d9d9d9;
  --white:#ffffff;
}
*{box-sizing:border-box;margin:0;padding:0}
html,body{width:1200px;height:3403px;overflow:hidden}
body{position:relative;background:var(--page);font-family:"Open Sans",sans-serif;color:var(--ink)}
.abs{position:absolute}
.center{text-align:center}
.brand{font-family:"Cinzel",serif;font-weight:500;color:var(--gold);letter-spacing:4px;white-space:nowrap}
.header-brand{left:0;width:1200px;top:56px;font-size:30px;text-align:center}
.header-icons{left:975px;top:46px}
.nav{left:0;top:129px;width:1200px;height:20px;font-family:"Roboto Slab",serif;font-size:11px;letter-spacing:.6px;color:var(--ink)}
.nav span{position:absolute;transform:translateX(-50%);white-space:nowrap}
.nav .active{color:var(--gold)}
.nav-underline{left:226px;top:154px;width:50px;height:1px;background:var(--gold)}
.media{background:linear-gradient(135deg,#b9a88d,#6e5a3d)}
.hero{left:10px;top:172px;width:1175px;height:480px;background:linear-gradient(100deg,#d8d2c8 0%,#b59a6a 35%,#8c6b3e 55%,#cbc3b6 80%,#dcd6cc 100%)}
.hero-title{right:108px;top:398px;text-align:right;font-family:"Roboto Slab",serif;font-weight:700;font-size:31px;line-height:37px;color:var(--white);letter-spacing:.5px;text-shadow:0 1px 2px rgba(0,0,0,.35)}
.hero-title .amp{color:var(--gold)}
.arrow{stroke:var(--ink);stroke-width:1.5;fill:none}
.eyebrow{font-family:"Playfair Display",serif;font-style:italic;color:var(--gold);font-size:17px;left:0;width:1200px;text-align:center}
.section-title{font-family:"Roboto Slab",serif;font-weight:300;font-size:32px;letter-spacing:2px;left:0;width:1200px;text-align:center;color:var(--ink)}
.rule{height:1px;background:var(--rule)}
.card{width:222px}
.card-media{position:absolute;left:0;top:0;width:222px;height:350px}
.card-label{position:absolute;left:14px;top:283px;width:195px;height:67px;background:var(--white);text-align:center}
.card-label em{display:block;font-family:"Playfair Display",serif;font-size:13px;color:var(--gold);margin-top:14px}
.card-label b{display:block;font-family:"Roboto Slab",serif;font-weight:400;font-size:16px;letter-spacing:.5px;margin-top:4px}
.card-text{position:absolute;top:368px;left:0;width:222px;font-family:"Roboto Slab",serif;font-weight:300;font-size:11.5px;line-height:24px;color:var(--muted)}
.card-more{position:absolute;top:446px;left:38px;font-size:11.5px;font-weight:600;letter-spacing:.6px;color:var(--ink)}
.card-more::before{content:"";display:inline-block;width:30px;height:1px;background:var(--rule);vertical-align:middle;margin-right:12px}
.sale{left:116px;top:1442px;width:966px;height:465px;background:linear-gradient(120deg,#5a4f44 0%,#3b342d 45%,#6b5a35 80%,#3a332c 100%)}
.sale-brand{font-family:"Playfair Display",serif;font-style:italic;font-size:22px;color:var(--gold);left:116px;width:966px;top:1580px}
.sale-title{font-family:"Roboto Slab",serif;font-weight:300;font-size:40px;color:var(--white);letter-spacing:1px;left:116px;width:966px;top:1614px}
.sale-text{left:116px;width:966px;top:1670px;font-size:12px;line-height:21px;color:var(--white)}
.btn{border:1px solid currentColor;font-family:"Roboto Slab",serif;font-size:10.5px;font-weight:700;letter-spacing:.4px;display:flex;align-items:center;justify-content:center}
.btn-light{left:559px;top:1738px;width:108px;height:38px;color:var(--white)}
.btn-gold{left:544px;top:2749px;width:110px;height:40px;color:var(--gold)}
.btn-gold span{color:var(--ink)}
.product{width:313px}
.product-media{position:absolute;left:0;top:0;width:313px;height:417px}
.product-name{position:absolute;top:444px;left:0;width:313px;text-align:center;font-family:"Roboto Slab",serif;font-size:16px;color:var(--ink)}
.product-price{position:absolute;top:472px;left:0;width:313px;text-align:center;font-family:"Roboto Slab",serif;font-size:15px;color:var(--gold)}
.dot{width:4px;height:4px;border-radius:50%;background:#b5b5b5}
.dot.on{width:6px;height:6px;background:#777}
.join{left:0;top:2844px;width:1200px;height:225px;background:var(--band)}
.join-title{left:0;width:1200px;top:2888px;font-family:"Roboto Slab",serif;font-weight:700;font-size:24px;color:var(--ink)}
.join-sub{left:0;width:1200px;top:2941px;font-size:12px;color:var(--ink)}
.join-field{left:439px;top:2989px;width:308px;height:32px;background:var(--white);font-size:9px;color:#aaa;padding:10px 22px}
.footer{left:0;top:3069px;width:1200px;height:334px;background:var(--footer)}
.footer-brand{left:0;width:1200px;top:3137px;font-size:28px;text-align:center}
.footer-col{font-family:"Roboto Slab",serif;font-size:12px;color:var(--footer-ink);letter-spacing:.3px}
.footer-col p{white-space:nowrap}
.contact p{line-height:32px}
.links p{line-height:26.5px;font-size:11.5px}
.social circle{fill:none;stroke:var(--footer-ink);stroke-width:1}
.to-top{left:1142px;top:3344px;width:40px;height:40px;background:#3c3c3c}
</style>
</head>
<body>

<header>
  <div class="abs brand header-brand">Larkmoor Lane</div>
  <svg class="abs header-icons" width="112" height="24" viewBox="0 0 112 24" aria-label="Cart, search and menu">
    <rect x="4" y="8" width="11" height="11" fill="none" stroke="#555" stroke-width="1.2"/>
    <path d="M6.5 8 V5.5 a3 3 0 0 1 6 0 V8" fill="none" stroke="#555" stroke-width="1.2"/>
    <text x="17" y="8" font-size="7" fill="#555" font-family="Open Sans">0</text>
    <circle cx="50" cy="11" r="5" fill="none" stroke="#555" stroke-width="1.3"/>
    <line x1="54" y1="15" x2="58" y2="19" stroke="#555" stroke-width="1.3"/>
    <line x1="85" y1="10" x2="107" y2="10" stroke="#555" stroke-width="1"/>
    <line x1="89" y1="15" x2="107" y2="15" stroke="#555" stroke-width="1"/>
  </svg>
  <nav class="abs nav">
    <span class="active" style="left:251px">HOME</span>
    <span style="left:383px">ANTIQUE &amp; VINTAGE</span>
    <span style="left:558px">ANTIQUE JEWELLERY</span>
    <span style="left:682px">ART</span>
    <span style="left:777px">FURNISHING</span>
    <span style="left:878px">OTHERS</span>
    <span style="left:962px">SALE</span>
  </nav>
  <div class="abs nav-underline"></div>
</header>

<section>
  <div class="abs hero" role="img" aria-label="Gilded star crown resting on antique leather-bound books against a marble wall"></div>
  <h1 class="abs hero-title">ANTIQUES <span class="amp">&amp;</span> BEAUTIFUL FINDS<br>FROM AROUND THE WORLD</h1>
  <svg class="abs" style="left:56px;top:408px" width="18" height="32"><path class="arrow" d="M15 2 L3 16 L15 30"/></svg>
  <svg class="abs" style="left:1128px;top:408px" width="18" height="32"><path class="arrow" d="M3 2 L15 16 L3 30"/></svg>
</section>

<section>
  <div class="abs eyebrow" style="top:736px">Unique &amp; Memorable</div>
  <h2 class="abs section-title" style="top:767px">OUR COLLECTION</h2>
  <div class="abs rule" style="left:313px;top:787px;width:87px"></div>
  <div class="abs rule" style="left:801px;top:787px;width:87px"></div>

  <article class="abs card" style="left:116px;top:843px;height:470px">
    <div class="card-media" role="img" aria-label="Wood-panelled hallway with staircase and crystal chandelier" style="background:linear-gradient(160deg,#c9a27a,#6a3a1e 60%,#3a2214)"></div>
    <div class="card-label"><em>Collection</em><b>ANTIQUE &amp; VINTAGE</b></div>
    <p class="card-text">Lorem ipsum dolor sit amet eiusmod, consectetur adip isi cing elit, sed do.</p>
    <div class="card-more">View more</div>
  </article>
  <article class="abs card" style="left:365px;top:843px;height:470px">
    <div class="card-media" role="img" aria-label="Slender brass sculpture on a pale background" style="background:linear-gradient(180deg,#e2dccd,#cdbf9f 70%,#b6a57a)"></div>
    <div class="card-label"><em>Collection</em><b>ART &amp; DECORATION</b></div>
    <p class="card-text">Lorem ipsum dolor sit amet eiusmod, consectetur adip isi cing elit, sed do.</p>
    <div class="card-more">View more</div>
  </article>
  <article class="abs card" style="left:613px;top:843px;height:470px">
    <div class="card-media" role="img" aria-label="Framed embroidered textile above a dark wooden chest with a plant" style="background:linear-gradient(180deg,#b49463,#8c6a3a 55%,#2f2a28)"></div>
    <div class="card-label"><em>Collection</em><b>FURNISHING</b></div>
    <p class="card-text">Lorem ipsum dolor sit amet eiusmod, consectetur adip isi cing elit, sed do.</p>
    <div class="card-more">View more</div>
  </article>
  <article class="abs card" style="left:862px;top:843px;height:470px">
    <div class="card-media" role="img" aria-label="Jewelled silver crown on a stand" style="background:linear-gradient(180deg,#d8d0c4,#6f6658 55%,#3f3a36)"></div>
    <div class="card-label"><em>Collection</em><b>JEWELLERY</b></div>
    <p class="card-text">Lorem ipsum dolor sit amet eiusmod, consectetur adip isi cing elit, sed do.</p>
    <div class="card-more">View more</div>
  </article>
</section>

<section>
  <div class="abs sale" role="img" aria-label="Shelves of rolled ribbons, trims and fabrics"></div>
  <div class="abs sale" style="background:rgba(0,0,0,.25)"></div>
  <div class="abs center sale-brand">Larkmoor Lane</div>
  <h2 class="abs center sale-title">COLLECTION SALE</h2>
  <p class="abs center sale-text">Lorem ipsum dolor sit amet, consectetur adipisicing elit, sed do eius<br>mod tempor incididunt ut labore et dolore magna aliqua.</p>
  <div class="abs btn btn-light">SHOP NOW</div>
</section>

<section>
  <div class="abs eyebrow" style="top:2039px">Our Latest Collection</div>
  <h2 class="abs section-title" style="top:2070px">NEW ARRIVALS</h2>
  <div class="abs rule" style="left:333px;top:2089px;width:85px"></div>
  <div class="abs rule" style="left:782px;top:2089px;width:86px"></div>

  <article class="abs product" style="left:108px;top:2173px;height:500px">
    <div class="product-media" role="img" aria-label="Fur hat with gilded trim on a stack of design books" style="background:linear-gradient(180deg,#c8c0b4,#6d6254 55%,#2d2a2a)"></div>
    <div class="product-name">Antique Item</div>
    <div class="product-price">$800.00</div>
  </article>
  <article class="abs product" style="left:441px;top:2173px;height:500px">
    <div class="product-media" role="img" aria-label="Gilded star crown on antique books" style="background:linear-gradient(180deg,#d6d1c9,#9c7c48 50%,#4a2f22)"></div>
    <div class="product-name">Antique Item</div>
    <div class="product-price">$1085.00</div>
  </article>
  <article class="abs product" style="left:769px;top:2173px;height:500px">
    <div class="product-media" role="img" aria-label="Embroidered gold bullion badge on black felt" style="background:radial-gradient(ellipse at center,#5a4a2a 0%,#1e1c1a 45%,#d9d4cc 70%)"></div>
    <div class="product-name">Antique Item</div>
    <div class="product-price">$568.00</div>
  </article>

  <svg class="abs" style="left:50px;top:2385px" width="14" height="26"><path class="arrow" d="M12 2 L2 13 L12 24"/></svg>
  <svg class="abs" style="left:1124px;top:2385px" width="14" height="26"><path class="arrow" d="M2 2 L12 13 L2 24"/></svg>

  <div class="abs dot" style="left:569px;top:2705px"></div>
  <div class="abs dot on" style="left:597px;top:2704px"></div>
  <div class="abs dot" style="left:627px;top:2705px"></div>

  <div class="abs btn btn-gold"><span>VIEW MORE</span></div>
</section>

<section>
  <div class="abs join"></div>
  <h2 class="abs center join-title">JOIN EMAIL</h2>
  <p class="abs center join-sub">Sign up to receive the latest news and updates</p>
  <div class="abs join-field">Your email address</div>
  <svg class="abs" style="left:718px;top:2997px" width="12" height="16"><path d="M2 1 L10 8 L2 15" fill="none" stroke="#333" stroke-width="1.6"/></svg>
</section>

<footer>
  <div class="abs footer"></div>
  <div class="abs brand footer-brand">Larkmoor Lane</div>
  <div class="abs footer-col contact" style="left:118px;top:3215px">
    <p>418 Hollin Row Westbrook</p>
    <p>555-014-2276, 555-019-3841</p>
    <p>hello@larkmoorlane.shop</p>
    <p>Copyright © Fernhall Studio 2019</p>
  </div>
  <div class="abs footer-col links" style="left:435px;top:3217px">
    <p>Antique &amp; Vintage</p><p>Jewellery</p><p>Art</p><p>Furnishing</p><p>Others</p>
  </div>
  <div class="abs footer-col links" style="left:637px;top:3217px">
    <p>Terms &amp; Conditions</p><p>Privacy Policy</p><p>Refund Policy</p><p>My Account</p>
  </div>
  <div class="abs footer-col" style="left:867px;top:3222px;font-weight:700">Follow Us At:</div>
  <svg class="abs social" style="left:864px;top:3252px" width="172" height="30" aria-label="Social links">
    <circle cx="16" cy="15" r="13"/><circle cx="50" cy="15" r="13"/><circle cx="85" cy="15" r="13"/><circle cx="119" cy="15" r="13"/><circle cx="154" cy="15" r="13"/>
  </svg>
  <div class="abs to-top"></div>
  <svg class="abs" style="left:1154px;top:3358px" width="16" height="10"><path d="M1 9 L8 2 L15 9" fill="none" stroke="#bbb" stroke-width="1.2"/></svg>
</footer>

</body>
</html>
```